Falcon guarding business card

Looking for a business card for my security company

Target Market(s)

Security

Industry/Entity Type

Security

Contact Information for Business Card

Name - Dale Hutchins. Title - General manager - direct 318 642.9053 website www. falconguardingservices.example email - dale@ falconguardingservices.example

Requirements
Must have
• Logo attached

```html
<!DOCTYPE html>
<html lang="en">
<head>
<meta charset="utf-8">
<title>Falcon Guarding Business Card</title>
<link href="https://fonts.googleapis.com/css2?family=Roboto+Condensed:wght@400;700&family=Roboto:wght@400;500&display=swap" rel="stylesheet">
<style>
  :root {
    --gold: #b07b2e;
    --gold-deep: #9a6a22;
    --ink: #1e1e1e;
    --paper: #ffffff;
    --backdrop: #1a1a1a;
  }
  html, body {
    margin: 0;
    width: 1200px;
    height: 900px;
    overflow: hidden;
    background: var(--backdrop);
  }
  .canvas {
    position: relative;
    width: 1200px;
    height: 900px;
  }
  .card {
    position: absolute;
    width: 560px;
    height: 320px;
    border-radius: 22px;
    overflow: hidden;
    box-shadow: 0 12px 30px rgba(0,0,0,.45);
  }
  .card--front { left: 40px; top: 290px; background: var(--paper); }
  .card--back  { left: 600px; top: 290px; background: var(--gold); }

  .brand {
    font-family: "Roboto Condensed", sans-serif;
    font-weight: 700;
    text-transform: uppercase;
    line-height: 1;
    text-align: center;
  }
  .card--front .brand {
    position: absolute;
    left: 30px; top: 118px;
    width: 220px;
    color: var(--gold);
    font-size: 38px;
    letter-spacing: 1px;
  }
  .card--back .brand {
    position: absolute;
    left: 0; right: 0; top: 120px;
    color: var(--paper);
    font-size: 62px;
    letter-spacing: 2px;
  }
  .divider {
    position: absolute;
    left: 268px; top: 70px;
    width: 2px; height: 180px;
    background: var(--gold);
  }
  .contact {
    position: absolute;
    left: 292px; top: 84px;
    font-family: "Roboto", sans-serif;
    color: var(--ink);
  }
  .contact__name {
    font-family: "Roboto Condensed", sans-serif;
    font-weight: 700;
    font-size: 28px;
    color: var(--gold);
    text-transform: uppercase;
    margin: 0;
  }
  .contact__title {
    font-family: "Roboto Condensed", sans-serif;
    font-size: 15px;
    text-transform: uppercase;
    margin: 2px 0 22px;
  }
  .contact__list { list-style: none; margin: 0; padding: 0; }
  .contact__item {
    display: flex;
    align-items: center;
    gap: 10px;
    font-size: 13px;
    margin-bottom: 12px;
  }
  .contact__item svg { width: 16px; height: 16px; flex: none; }
</style>
</head>
<body>
<div class="canvas">
  <section class="card card--front">
    <div class="brand">Falcon Guarding</div>
    <div class="divider"></div>
    <div class="contact">
      <h1 class="contact__name">Dale Hutchins</h1>
      <div class="contact__title">General Manager</div>
      <ul class="contact__list">
        <li class="contact__item">
          <svg viewBox="0 0 16 16"><path d="M4 1.5l2.2 3-1.3 1.4c.8 1.8 2.3 3.3 4.2 4.2l1.4-1.3 3 2.2-1.2 2.5C7.2 13.3 2.7 8.8 1.5 3.7z" fill="var(--gold)"/></svg>
          318 642.9053
        </li>
        <li class="contact__item">
          <svg viewBox="0 0 16 16"><rect x="1" y="3" width="14" height="10" fill="var(--gold)"/><path d="M1 3l7 6 7-6" fill="none" stroke="#fff" stroke-width="1.2"/></svg>
          dale@falconguardingservices.example
        </li>
        <li class="contact__item">
          <svg viewBox="0 0 16 16"><circle cx="8" cy="8" r="7" fill="var(--gold)"/><g fill="none" stroke="#fff" stroke-width="1"><ellipse cx="8" cy="8" rx="3" ry="7"/><path d="M1 8h14M2.5 4.5h11M2.5 11.5h11"/></g></svg>
          www.falconguardingservices.example
        </li>
      </ul>
    </div>
  </section>

  <section class="card card--back">
    <div class="brand">Falcon Guarding</div>
  </section>
</div>
</body>
</html>
```